Home page web design for a lawn specialist business

-The design must be based around the attached HPID (home page information design) called Turf Haven HPID. I've attached Word and PDF versions - these are the same. The table boxes are just for approximate placement of information and you can use boxes and bold shapes for this design.

All fonts used in the HPID are only examples - you can use any Google font you wish.

- Text that is in orange is for your information only. Text to go on the design is black. Some instructions are in the HPID. Please be creative!

-The design needs to be modern and exciting - colours are to be the green of the logo, and white ...and then choose dark green, or dark grey or black.

Logo - attached (it's not great quality but don't worry, we'll replace it later)

- I've provided the images for the galleries - they are labelled and will match the name in the HPID. Please use the supplied images!

- Examples of some websites that have great design... don't copy them please but they are similar in look to what we are after....
www.kelbrinworks.co.nz
http://www.rimsafe-guarding.co.nz/
http://www.brightnest.wb.gs/

Important: Width of content will be 1280 pixels when implemented as a web page but the winning design will need to supplied be on a 2000 pixel wide background so nav bars and background can extend outside the 1280 width.
Header height (without nav bar) 150-160 pixels.

We don't comment on individual designs but will choose a winning design promptly.

Industry/Entity Type

Business

Number of Pages Required

1 page

Font styles to use
Sans Serif

Requirements
Must have
• clean, modern, well-spaced design

```html
<!DOCTYPE html>
<html lang="en">
<head>
<meta charset="utf-8">
<title>Turf Haven – Lawn Specialists</title>
<link rel="stylesheet" href="https://fonts.googleapis.com/css2?family=Questrial&family=Open+Sans:wght@400;600&display=swap">
<style>
:root{
  --green:#3fa32c;
  --green-bright:#5cc13a;
  --green-dark:#1f5a17;
  --green-deep:#12330e;
  --charcoal:#3a3a3a;
  --charcoal-dark:#2b2b2b;
  --grey-panel:#c9c9c9;
  --text:#3d3d3d;
  --white:#ffffff;
}
*{box-sizing:border-box;margin:0;padding:0}
html,body{width:1200px;height:3881px;overflow:hidden}
body{background:var(--white);font-family:"Open Sans",sans-serif;color:var(--text);position:relative}
.heading{font-family:"Questrial",sans-serif}

.grass-strip{position:absolute;left:0;top:0;width:1200px;height:80px;background:linear-gradient(180deg,#ffffff 0%,#9fd47c 55%,#3f8f27 100%)}
.brand{position:absolute;left:58px;top:100px;display:flex;align-items:center;gap:14px}
.brand-square{width:110px;height:110px;background:var(--green)}
.brand-name{font-family:"Questrial",sans-serif;font-size:40px;color:var(--green-dark)}
.header-info{position:absolute;right:58px;top:96px;text-align:right;font-family:"Questrial",sans-serif;color:#222}
.header-info .title{font-size:44px;line-height:52px}
.header-info .tagline{font-size:17px;margin-top:4px}
.header-info .region{font-size:30px;margin-top:8px}
.header-info .phone{font-size:32px;margin-top:4px;display:flex;justify-content:flex-end;align-items:center;gap:10px}

.main-nav{position:absolute;left:0;top:307px;width:1200px;height:36px;background:linear-gradient(180deg,#2f7a22,var(--green-deep));display:flex;padding:0 58px}
.main-nav a{flex:1;color:#e9f5e4;font-size:11px;text-decoration:none;text-align:center;line-height:36px;border-right:1px solid rgba(255,255,255,.2);text-transform:uppercase}
.main-nav a.active{background:var(--green-bright)}

.hero{position:absolute;left:0;top:350px;width:1200px;height:460px;background:linear-gradient(100deg,#b9b2a4 0%,#8a7b66 35%,#6fa84a 55%,#4f9a2f 100%)}
.hero-badge{position:absolute;width:140px;height:140px;border-radius:50%;background:var(--charcoal-dark);color:#fff;font-family:"Questrial",sans-serif;font-size:26px;display:flex;align-items:center;justify-content:center;top:320px}
.hero-shadow{position:absolute;left:100px;top:810px;width:1000px;height:30px;background:radial-gradient(ellipse at top,rgba(0,0,0,.25),transparent 70%)}

.intro{position:absolute;left:50px;top:890px;width:1100px;text-align:center}
.intro h1{font-family:"Questrial",sans-serif;font-weight:400;color:var(--green);font-size:38px;line-height:44px}
.intro h2{font-family:"Questrial",sans-serif;font-weight:400;font-size:24px;color:#333}
.intro p{text-align:left;font-size:15px;line-height:22px;margin-top:18px}

.service{position:absolute;width:505px;height:545px;overflow:hidden;box-shadow:0 4px 10px rgba(0,0,0,.25)}
.service-photo{position:absolute;inset:0}
.service-panel{position:absolute;inset:0;background:linear-gradient(180deg,#e2e2e2,var(--grey-panel) 60%,#9d9d9d);clip-path:polygon(50% 0,100% 0,100% 100%,22% 100%)}
.service-body{position:absolute;right:30px;top:50px;width:215px;text-align:right}
.service-body h3{font-family:"Questrial",sans-serif;font-weight:400;font-size:26px;line-height:30px;color:#222}
.service-body h3::after{content:"";display:block;width:160px;height:2px;background:#555;margin:12px 0 0 auto}
.service-body p{font-size:16px;line-height:22px;margin-top:70px;color:#333}
.read-more{position:absolute;right:30px;bottom:30px;background:#4a4a4a;color:#fff;font-size:16px;padding:8px 18px;border-radius:4px;display:flex;gap:10px;align-items:center}

.video-title{position:absolute;left:60px;top:2290px;width:540px;text-align:center;font-family:"Questrial",sans-serif;font-size:26px;line-height:32px;color:#222}
.video-title span{color:var(--green)}
.video{position:absolute;left:80px;top:2395px;width:502px;height:290px;background:linear-gradient(180deg,#9fa88d,#5f8a3c 60%,#3d6a25)}
.video-bar{position:absolute;left:0;bottom:0;width:100%;height:26px;background:#111}
.about-circle{position:absolute;left:615px;top:2300px;width:480px;height:480px;border-radius:50%;background:radial-gradient(circle at 50% 40%,#2f7a22,var(--green-deep));box-shadow:0 6px 16px rgba(0,0,0,.35);text-align:center;color:#fff;padding:70px 80px 0}
.about-circle h3{font-family:"Questrial",sans-serif;font-weight:400;font-size:34px}
.about-circle h3::after{content:"";display:block;width:240px;height:2px;background:#fff;margin:10px auto 18px}
.about-circle p{font-size:16px;line-height:22px}
.about-circle .cta{display:inline-block;margin-top:20px;background:var(--green-bright);color:#fff;padding:10px 20px;border-radius:6px;font-size:16px}

.testimonial{position:absolute;left:0;top:2782px;width:1200px;height:390px;background:linear-gradient(90deg,#2a3a24,#4d5e3e 50%,#3a4a30)}
.testimonial h2{position:absolute;left:0;width:100%;top:70px;text-align:center;font-family:"Questrial",sans-serif;font-weight:400;font-size:46px;color:#fff}
.testimonial h2::after{content:"";display:block;width:150px;height:3px;background:#fff;margin:8px auto 0}
.testimonial blockquote{position:absolute;left:190px;top:185px;width:900px;font-family:"Questrial",sans-serif;font-size:34px;line-height:44px;color:#fff}
.testimonial .q{font-size:80px;line-height:0;vertical-align:-28px}
.testimonial cite{position:absolute;right:180px;top:320px;font-style:normal;font-family:"Questrial",sans-serif;font-size:26px;color:#fff;line-height:30px}

.footer{position:absolute;left:0;top:3172px;width:1200px;height:709px;background:var(--charcoal)}
.footer-nav{position:absolute;left:58px;top:155px;list-style:none;font-family:"Questrial",sans-serif;font-size:34px;line-height:38px;color:#fff}
.cert-badge{position:absolute;left:445px;top:190px;width:180px;height:180px;border-radius:50%;background:var(--green)}
.quote-intro{position:absolute;left:770px;top:55px;width:380px;text-align:center;color:#fff;font-family:"Questrial",sans-serif;font-size:19px;line-height:24px}
.quote-intro .num{color:var(--green-bright);font-size:30px;display:block;margin-top:8px}
.quote-form{position:absolute;left:750px;top:175px;width:390px;height:410px;background:var(--green-dark);padding:16px}
.quote-form h4{font-family:"Questrial",sans-serif;font-weight:400;color:#cfe7c6;font-size:18px;border-bottom:1px solid rgba(255,255,255,.3);padding-bottom:8px}
.field{height:24px;background:#2f7a22;border:1px solid #5a9a4c;color:#e3f0de;font-size:11px;padding:4px 6px;margin-top:12px}
.row{display:flex;gap:12px}
.row .field{flex:1}
.field.details{height:190px}
.send{position:absolute;right:16px;bottom:14px;background:#e3e3e3;color:#333;font-size:11px;padding:4px 10px}
</style>
</head>
<body>

<div class="grass-strip" role="img" aria-label="Grass blades along the top edge"></div>

<header>
  <div class="brand"><div class="brand-square"></div><span class="brand-name">Turf Haven</span></div>
  <div class="header-info">
    <div class="title">LAWN SPECIALISTS</div>
    <div class="tagline">...FROM GROUND PREPARATION TO LAWN AFTERCARE</div>
    <div class="region">SERVICING THE AUCKLAND REGION</div>
    <div class="phone">
      <svg width="30" height="30" viewBox="0 0 30 30"><circle cx="15" cy="15" r="15" fill="#3fa32c"/><path d="M10 8c1-1 2 0 3 2s0 2-1 3c1 2 3 4 5 5 1-1 1-2 3-1s3 2 2 3c-1 2-3 3-6 1s-6-5-7-8 0-4 1-5z" fill="#fff"/></svg>
      0800 41 62 90
    </div>
  </div>
</header>

<nav class="main-nav">
  <a class="active">Home</a><a>About us</a><a>Services</a><a>Lawn care</a><a>Seasonal care</a><a>Hydroseeding</a><a>FAQs</a><a>Before &amp; after gallery</a><a>Quote / contact</a>
</nav>

<section class="hero" role="img" aria-label="Before and after photo of a garden: bare soil beds transformed into a lush green lawn">
  <div class="hero-badge heading" style="left:60px">BEFORE</div>
  <div class="hero-badge heading" style="left:725px">AFTER</div>
</section>
<div class="hero-shadow"></div>

<section class="intro">
  <h1>YOU CAN ALWAYS SPOT AN TURF HAVEN LAWN</h1>
  <h2>IT'S THE ONE THAT TURNS YOUR NEIGHBOURS GREEN WITH ENVY.</h2>
  <p>If you want a lawn or playing field that looks good throughout the year, talk to us. Turf Haven are New Zealand's experts in high quality grass seeding and lawn maintenance, creating the lushest lawns you'll ever see. With high-tech equipment, years of experience and expert aftercare, nobody knows grass like Turf Haven.</p>
  <p>There are many factors that influence the quality of a lawn, including seasonality, growing conditions, shade, seed types, and time. A one-size-fits-all solution couldn't possibly guarantee a great lawn, so we provide personalised advice, a full range of seeding techniques.</p>
</section>

<article class="service" style="left:80px;top:1132px">
  <div class="service-photo" role="img" aria-label="Freshly hydroseeded garden bed with tropical plants" style="background:linear-gradient(160deg,#6a8a4a,#2f7a6a 60%,#3c5a44)"></div>
  <div class="service-panel"></div>
  <div class="service-body"><h3>GRASS SEEDING SERVICES</h3><p>With a wide range of grass seed applications to choose from, including hydroseeding and instant lawn, there is an option to suit your property and your requirements.</p></div>
  <div class="read-more">READ MORE <span>›</span></div>
</article>

<article class="service" style="left:608px;top:1132px">
  <div class="service-photo" role="img" aria-label="Lawn sprinkler watering green grass" style="background:linear-gradient(160deg,#8fbf5a,#4f8f2f 60%,#2f5a1f)"></div>
  <div class="service-panel"></div>
  <div class="service-body"><h3>LAWN CARE MAINTENANCE</h3><p>As well as lawn care services, the team at Turf Haven provides helpful information for regular upkeep of your residential or commercial lawn.</p></div>
  <div class="read-more">READ MORE <span>›</span></div>
</article>

<article class="service" style="left:80px;top:1730px">
  <div class="service-photo" role="img" aria-label="Green lawn beside a tree and fence" style="background:linear-gradient(160deg,#9aa58a,#5f9a38 55%,#3f7a25)"></div>
  <div class="service-panel"></div>
  <div class="service-body"><h3>FAQS ABOUT GRASS SEEDING AND LAWN CARE</h3><p>For more information, read our frequently asked questions regarding grass seeding and lawn care.</p></div>
  <div class="read-more">READ MORE <span>›</span></div>
</article>

<article class="service" style="left:608px;top:1730px">
  <div class="service-photo" role="img" aria-label="Backyard lawn before and after seeding" style="background:linear-gradient(180deg,#a89e88,#2f7a6a 45%,#5f9a38 60%,#4f8a2f)"></div>
  <div class="service-panel"></div>
  <div class="service-body"><h3>BEFORE AND AFTER LAWN PHOTOS</h3><p>See what your potential new lawn could look like by viewing a range of before and after lawn seeding photos.</p></div>
  <div class="read-more">READ MORE <span>›</span></div>
</article>

<h3 class="video-title">WATCH THE VIDEO ON HOW TURF HAVEN CAN TRANSFORM YOUR EMPTY SPACES INTO <span>BEAUTIFUL GREEN GRASS LAWNS</span></h3>
<div class="video" role="img" aria-label="Video still of a new lawn in a suburban garden">
  <div class="video-bar"></div>
</div>

<section class="about-circle">
  <h3>TURF HAVEN...</h3>
  <p>For all things grass, you need the best! Turf Haven are skilled specialists when it comes to creating the perfect lawn for your property. From pre-seeding preparation to a full range of grass seeding services and lawn after care options, you'll enjoy a healthy green lawn for many years.<br>Selling your property? Turf Haven will add the wow factor to the outdoor areas of your home with a lush green lawn.</p>
  <span class="cta">Find out more</span>
</section>

<section class="testimonial" role="img" aria-label="Lawn mower on a freshly cut lawn, darkened backdrop">
  <h2>TESTIMONIAL</h2>
  <blockquote><span class="q">“</span> "I WOULD RECOMMEND TURF HAVEN TO ANYONE WHO WANTS AN AMAZING LAWN" <span class="q">”</span></blockquote>
  <cite>Dan Porter<br>Homeowner, Albany</cite>
</section>

<footer class="footer">
  <ul class="footer-nav">
    <li>HOME</li><li>ABOUT US</li><li>SERVICES</li><li>LAWN CARE</li><li>SEASONAL CARE</li><li>HYDROSEEDING</li><li>FAQS</li><li>BEFORE &amp; AFTER</li><li>GALLERY</li><li>QUOTE / CONTACT</li>
  </ul>
  <div class="cert-badge" role="img" aria-label="Horticulture qualification badge"></div>
  <div class="quote-intro">GET A QUOTE FOR YOUR NEW LAWN! FILL IN THE FORM OR PHONE US ON 0 <span class="num">800 41 62 90.</span></div>
  <form class="quote-form">
    <h4>GET A QUOTE</h4>
    <div class="row"><div class="field">First name</div><div class="field">Last name</div></div>
    <div class="row"><div class="field">Email address</div><div class="field" style="visibility:hidden"></div></div>
    <div class="row"><div class="field">Contact phone</div><div class="field" style="visibility:hidden"></div></div>
    <div class="field details">Details</div>
    <div class="send">CALL ME BACK</div>
  </form>
</footer>

</body>
</html>
```